An innovative software company needs a business card!

We need a business card design for our new innovative software company. Please use the details for the business card provided in business card details section. We will use the business card paper like: https://www.plavex.com/us/products/nfc/business-cards-plus.html Our company name: kelvora We have already a logo and colors to use in business cards too ,

Target Market(s)

App & Sofware Development

Industry/Entity Type

Software

Contact Information for Business Card

Lukas Brenner, BSc.
Owner and Creative Superhero

Adress:
Tulpenweg 37/4/1809
A - 1100, Wien

Tel: +43 (0) 676 921 35 60
Email: lukas.brenner@kelvora.at
Web: www.kelvora.at

Requirements
Must have
• - Use our logo
Nice to have
• It would be nice to have a nice picture on the backside. (About apps, software, technicals or funy stuff) - Use our colors as in business card (optional)

```html
<!DOCTYPE html>
<html lang="en">
<head>
<meta charset="utf-8">
<title>kelvora business card</title>
<link href="https://fonts.googleapis.com/css2?family=Roboto+Condensed:wght@400;700&family=Roboto:wght@400;700&display=swap" rel="stylesheet">
<style>
  :root {
    --canvas: #eef0f1;
    --card: #050505;
    --blue: #1e9ad6;
    --white: #ffffff;
    --faint: #151515;
    --grey: #b9bcbf;
  }
  * { margin: 0; padding: 0; box-sizing: border-box; }
  html, body { width: 1200px; height: 904px; overflow: hidden; background: var(--canvas); }
  .sheet {
    width: 1200px; height: 904px;
    display: flex; flex-direction: column; align-items: center; justify-content: center; gap: 44px;
  }
  .card {
    position: relative; width: 620px; height: 400px;
    background: var(--card); overflow: hidden;
    box-shadow: 0 10px 26px rgba(0,0,0,.18);
  }
  /* front */
  .stripe { position: absolute; background: var(--blue); }
  .stripe--left-a { left: 22px; top: 0; width: 9px; height: 190px; }
  .stripe--left-b { left: 44px; top: 0; width: 9px; height: 190px; }
  .stripe--right-a { right: 0; top: 178px; width: 56px; height: 8px; }
  .stripe--right-b { right: 0; top: 196px; width: 56px; height: 8px; }
  .holder { position: absolute; left: 78px; top: 42px; color: var(--white); font-family: "Roboto Condensed", sans-serif; }
  .holder__name { font-weight: 700; font-size: 31px; letter-spacing: .5px; text-transform: uppercase; line-height: 1; }
  .holder__role { font-size: 12.5px; text-transform: uppercase; margin-top: 4px; letter-spacing: .3px; }
  .brand { position: absolute; display: flex; align-items: center; gap: 12px; font-family: "Roboto", sans-serif; font-weight: 700; color: var(--blue); }
  .brand--front { right: 74px; top: 172px; font-size: 40px; }
  .brand__dot { width: 30px; height: 30px; border-radius: 50%; background: var(--blue); }
  .contacts { position: absolute; left: 78px; bottom: 34px; list-style: none; font-family: "Roboto", sans-serif; color: var(--white); font-size: 15.5px; }
  .contacts li { display: flex; align-items: center; gap: 14px; height: 36px; }
  .contacts svg { width: 26px; height: 26px; flex: none; }
  /* back */
  .tab { position: absolute; background: var(--blue); border-radius: 16px; }
  .tab--left { left: -30px; bottom: 54px; width: 120px; height: 54px; }
  .tab--right { right: -30px; top: 46px; width: 120px; height: 54px; }
  .halo { position: absolute; left: 250px; top: 40px; width: 330px; height: 330px; border-radius: 50%; background: var(--faint); }
  .brand--back { left: 50%; top: 50%; transform: translate(-50%, -50%); font-size: 86px; gap: 22px; }
  .brand--back .brand__dot { width: 64px; height: 64px; }
</style>
</head>
<body>
<main class="sheet">
  <section class="card card--front" aria-label="Card front">
    <span class="stripe stripe--left-a"></span>
    <span class="stripe stripe--left-b"></span>
    <span class="stripe stripe--right-a"></span>
    <span class="stripe stripe--right-b"></span>
    <div class="holder">
      <p class="holder__name">Lukas Brenner, BSc.</p>
      <p class="holder__role">Owner and Creative Superhero</p>
    </div>
    <div class="brand brand--front"><span class="brand__dot"></span>kelvora</div>
    <ul class="contacts">
      <li>
        <svg viewBox="0 0 26 26" aria-hidden="true"><circle cx="13" cy="13" r="13" fill="#1e9ad6"/><path d="M9 7.5c1 0 1.5 2.5 1.5 3s-1 1-1 1.5c.6 1.6 2 3 3.5 3.5.5 0 1-1 1.5-1s3 .5 3 1.5-1.2 2.5-2.5 2.5C10.5 18.5 7 15 7 10c0-1.3 1-2.5 2-2.5z" fill="#fff"/></svg>
        +43 (0) 676 921 35 60
      </li>
      <li>
        <svg viewBox="0 0 26 26" aria-hidden="true"><circle cx="13" cy="13" r="13" fill="#1e9ad6"/><rect x="6.5" y="8.5" width="13" height="9" fill="none" stroke="#fff" stroke-width="1.5"/><path d="M6.5 8.5l6.5 5 6.5-5" fill="none" stroke="#fff" stroke-width="1.5"/></svg>
        lukas.brenner@kelvora.at
      </li>
      <li>
        <svg viewBox="0 0 26 26" aria-hidden="true"><circle cx="13" cy="13" r="13" fill="#1e9ad6"/><g fill="none" stroke="#fff" stroke-width="1.3"><circle cx="13" cy="13" r="7"/><ellipse cx="13" cy="13" rx="3" ry="7"/><path d="M6 13h14M7 9.5h12M7 16.5h12"/></g></svg>
        www.kelvora.at
      </li>
      <li>
        <svg viewBox="0 0 26 26" aria-hidden="true"><circle cx="13" cy="13" r="13" fill="#1e9ad6"/><path d="M13 6a5 5 0 0 1 5 5c0 3.5-5 9-5 9s-5-5.5-5-9a5 5 0 0 1 5-5z" fill="#fff"/><circle cx="13" cy="11" r="1.8" fill="#1e9ad6"/></svg>
        Tulpenweg 37/4/1809 A - 1100, Wien
      </li>
    </ul>
  </section>

  <section class="card card--back" aria-label="Card back">
    <span class="halo"></span>
    <span class="tab tab--left"></span>
    <span class="tab tab--right"></span>
    <div class="brand brand--back"><span class="brand__dot"></span>kelvora</div>
  </section>
</main>
</body>
</html>
```